Paper and board wholesaler needs business card design for managers

We need a business card design that incorporates bordo red, white and/ or grey colors. The business card has to have our "VELON" logo and our partners paper group logo that we are part of - "ROSKU group". Both of the logos should be applied to the business card according to the guidelines for the usage of the logo that have been added in the uploaded files.
The letters (information on the card) should be easily readable, so no "shiny" or "glossy" text.
Besides the two logos, the business card needs to contain information for the respective person:
1) Name, Surname,
2) Job position (e.g. "sales represantative"),
3) E-mail,
4) Phone number,
5) text: "Kartonu Mājvieta (VELON)" LTD
6) our office address "Riga, Sārtaines street 42".
(also could have) 7) our homepage address "www.velon.lv"
Holiday season, so have a lot of tasks to take care of and not as much time to check SketchHarbor as often.
1) Name, Surname, 2) Job position (e.g. "sales represantative"), 3) E-mail, 4) Phone number, 5) text: "Kartonu Mājvieta (VELON)" LTD 6) our office address "Riga, Sārtaines street 42". (also could have) 7) our homepage address "www.velon.lv"
Other font styles liked:
- Josefin Sans

```html
<!DOCTYPE html>
<html lang="en">
<head>
<meta charset="utf-8">
<title>VELON business card</title>
<link rel="stylesheet" href="https://fonts.googleapis.com/css2?family=Montserrat:wght@400;500;700&display=swap">
<style>
  :root {
    --bordo: #843237;
    --paper: #ffffff;
    --ink: #1e1e1e;
    --backdrop: #3b3c3d;
  }
  * { margin: 0; padding: 0; box-sizing: border-box; }
  html, body { width: 1200px; height: 1059px; overflow: hidden; background: var(--backdrop); }
  body { position: relative; font-family: "Montserrat", Arial, sans-serif; }

  .card { position: absolute; width: 690px; height: 392px; box-shadow: 0 12px 30px rgba(0,0,0,.45); }
  .card--front { left: 256px; top: 100px; background: var(--paper); }
  .card--back { left: 254px; top: 537px; background: var(--bordo); }

  .brand { position: absolute; display: flex; align-items: center; }
  .brand__square { width: 70px; height: 70px; border: 3px solid currentColor; }
  .brand__name { font-weight: 500; font-size: 36px; letter-spacing: 35px; line-height: 1; }
  .card--front .brand { left: 24px; top: 73px; color: var(--bordo); }
  .card--front .brand__name { margin-left: 58px; }
  .card--back .brand { left: 136px; top: 158px; color: var(--paper); }
  .card--back .brand__square { width: 78px; height: 78px; }
  .card--back .brand__name { margin-left: 62px; font-size: 38px; letter-spacing: 38px; }

  .person__bar { position: absolute; left: 0; top: 213px; width: 13px; height: 42px; background: var(--bordo); }
  .person__name { position: absolute; left: 25px; top: 209px; font-size: 30px; font-weight: 700; color: var(--bordo); letter-spacing: .5px; }
  .person__role { position: absolute; left: 25px; top: 240px; font-size: 17px; color: var(--ink); }

  .contact { position: absolute; left: 23px; top: 287px; list-style: none; }
  .contact__item { display: flex; align-items: center; height: 26.5px; font-size: 16.5px; color: var(--ink); }
  .contact__icon { width: 14px; height: 14px; margin-right: 9px; fill: var(--bordo); }

  .divider { position: absolute; left: 272px; top: 321px; width: 1px; height: 38px; background: var(--bordo); }
  .company { position: absolute; left: 294px; top: 316px; font-size: 16.5px; }
  .company__name { color: var(--bordo); height: 24px; }
  .company__address { display: flex; align-items: center; color: var(--ink); }
  .company__pin { width: 12px; height: 16px; margin-right: 5px; fill: var(--bordo); }
</style>
</head>
<body>
  <section class="card card--front">
    <div class="brand"><span class="brand__square"></span><span class="brand__name">VELON</span></div>

    <span class="person__bar"></span>
    <h1 class="person__name">DAVIS KALNS</h1>
    <p class="person__role">Sales Represantative</p>

    <ul class="contact">
      <li class="contact__item">
        <svg class="contact__icon" viewBox="0 0 24 24"><path d="M6.6 10.8a15 15 0 0 0 6.6 6.6l2.2-2.2c.3-.3.7-.4 1-.2 1.1.4 2.3.6 3.6.6.6 0 1 .4 1 1V20c0 .6-.4 1-1 1C10.6 21 3 13.4 3 4c0-.6.4-1 1-1h3.5c.6 0 1 .4 1 1 0 1.2.2 2.4.6 3.6.1.3 0 .7-.2 1z"/></svg>
        123-456-7890
      </li>
      <li class="contact__item">
        <svg class="contact__icon" viewBox="0 0 24 24"><path d="M2 5h20v2l-10 6L2 7z M2 9l10 6 10-6v10H2z"/></svg>
        info@velon.lv
      </li>
      <li class="contact__item">
        <svg class="contact__icon" viewBox="0 0 24 24" fill="none" stroke="#843237" stroke-width="1.8"><circle cx="12" cy="12" r="9.5"/><ellipse cx="12" cy="12" rx="4" ry="9.5"/><path d="M2.5 12h19M4 7h16M4 17h16"/></svg>
        www.velon.lv
      </li>
    </ul>

    <span class="divider"></span>
    <div class="company">
      <p class="company__name">Kartonu Mājvieta (VELON)" LTD</p>
      <p class="company__address">
        <svg class="company__pin" viewBox="0 0 12 16"><path d="M6 0a6 6 0 0 0-6 6c0 4.5 6 10 6 10s6-5.5 6-10a6 6 0 0 0-6-6zm0 8.3A2.3 2.3 0 1 1 6 3.7a2.3 2.3 0 0 1 0 4.6z"/></svg>
        Riga, Sārtaines street 42
      </p>
    </div>
  </section>

  <section class="card card--back">
    <div class="brand"><span class="brand__square"></span><span class="brand__name">VELON</span></div>
  </section>
</body>
</html>
```